Business Card Design

We are a cutting edge natural health care provider who specializes in neuro behavioral conditions. We use brain mapping, neurofeedback, functional neurology and functional medicine to help people achieve their health goals.
We need a business card design for a new office. Would like to position ourselves as an upscale/concierge level treatment center that provides hope and results to people with chronic conditions. We would like the card to feature a brain, possibly a die cut shape. Design needs to communicate our tag line of "providing excellent care for difficult cases."
On back side of card:
By retraining abnormal brainwave patterns and eliminating metabolic problems, our programs often improve symptoms of:
ADD/ADHD
Addiction
Anxiety
Autism
Depression
Fibromyalgia
Insomnia
Memory Loss
Sensory/Motor Dysfunction

Target Market(s)

30-60 year olds with chronic conditions (Anxiety, depression,) or parents of children with chronic conditions (ADHD, autism, learning disorders, etc)

Industry/Entity Type

Health

Contact Information for Business Card

The Halvey Clinic
Dr. Colin Halvey, DC
2641 Orchard Pkwy. Suite 207
Duluth, GA 30097
(770) 555-0148
Fax (770) 555-0193
www.TheHalveyClinic.example
www.DrColinHalvey.example

Requirements
Nice to have
• Picture of a brain that really pops on the page.

```html
<!DOCTYPE html>
<html lang="en">
<head>
<meta charset="utf-8">
<title>The Halvey Clinic – Business Card</title>
<link rel="stylesheet" href="https://fonts.googleapis.com/css2?family=Tenor+Sans&display=swap">
<style>
  :root {
    --backdrop: #d9d9d9;
    --card-white: #f7f7f5;
    --lime: #b6cf2c;
    --lime-soft: #c4d84a;
    --sky: #8fd3ea;
    --aqua: #a6e0d8;
    --mint: #c8e6a8;
    --divider: rgba(255, 255, 255, 0.55);
    --ink-fill: #f3f1c8;
    --ink-edge: #4a5a3a;
  }
  * { box-sizing: border-box; margin: 0; padding: 0; }
  html, body {
    width: 1200px; height: 765px; overflow: hidden;
    background: var(--backdrop);
  }
  .card {
    position: absolute; left: 120px; top: 102px;
    width: 960px; height: 560px;
    background: var(--card-white);
    box-shadow: 0 6px 18px rgba(0,0,0,0.18);
  }
  .card__face {
    position: absolute; left: 28px; top: 28px;
    width: 904px; height: 504px; overflow: hidden;
  }
  .card__photo {
    position: absolute; inset: 0;
    background:
      radial-gradient(ellipse at 20% 80%, rgba(120,200,220,0.9), transparent 55%),
      radial-gradient(ellipse at 55% 35%, var(--mint), transparent 60%),
      linear-gradient(110deg, var(--sky) 0%, var(--aqua) 45%, var(--mint) 70%, var(--sky) 100%);
  }
  .block-lime-top {
    position: absolute; left: 0; top: 0;
    width: 280px; height: 240px;
    background: linear-gradient(135deg, var(--lime), var(--lime-soft));
  }
  .block-lime-bottom {
    position: absolute; right: 0; bottom: 0;
    width: 372px; height: 196px;
    background: linear-gradient(90deg, rgba(182,207,44,0.35), var(--lime) 40%);
  }
  .divider { position: absolute; background: var(--divider); }
  .divider--v1 { left: 280px; top: 0; width: 1px; height: 504px; }
  .divider--v2 { left: 700px; top: 0; width: 1px; height: 308px; }
  .divider--h  { left: 0; top: 240px; width: 904px; height: 1px; }
  .emboss {
    font-family: "Tenor Sans", sans-serif;
    color: var(--ink-fill);
    text-shadow:
      -1px -1px 0 var(--ink-edge), 1px -1px 0 var(--ink-edge),
      -1px 1px 0 var(--ink-edge), 1px 1px 0 var(--ink-edge),
      2px 2px 3px rgba(0,0,0,0.25);
    position: absolute; white-space: nowrap;
  }
  .identity { left: 300px; top: 36px; }
  .identity__doctor { font-size: 44px; letter-spacing: 1px; line-height: 1.1; }
  .identity__clinic { font-size: 40px; letter-spacing: 1px; line-height: 1.1; margin-left: 18px; }
  .identity__web { font-size: 24px; letter-spacing: 1px; margin-left: 10px; margin-top: 4px; }
  .contact { left: 470px; top: 292px; font-size: 27px; line-height: 1.3; letter-spacing: 0.5px; }
  .contact__line { display: flex; align-items: center; gap: 4px; }
  .contact__icon { width: 26px; height: 26px; }
</style>
</head>
<body>
  <div class="card">
    <div class="card__face">
      <div class="card__photo" role="img" aria-label="Soft blue-green photograph of a patient relaxing during a treatment session"></div>
      <div class="block-lime-top"></div>
      <div class="block-lime-bottom"></div>
      <div class="divider divider--v1"></div>
      <div class="divider divider--v2"></div>
      <div class="divider divider--h"></div>

      <div class="identity emboss">
        <p class="identity__doctor">Dr. Colin Halvey</p>
        <p class="identity__clinic">The Halvey Clinic</p>
        <p class="identity__web">www.TheHalveyClinic.example</p>
      </div>

      <div class="contact emboss">
        <p class="contact__line">DC 2641 Orchard Pkwy.</p>
        <p class="contact__line">Suite 207 Duluth,</p>
        <p class="contact__line">
          <svg class="contact__icon" viewBox="0 0 24 24" aria-hidden="true">
            <path d="M6.6 10.8c1.4 2.8 3.8 5.1 6.6 6.6l2.2-2.2c.3-.3.7-.4 1-.2 1.1.4 2.3.6 3.6.6.6 0 1 .4 1 1V20c0 .6-.4 1-1 1C10.6 21 3 13.4 3 4c0-.6.4-1 1-1h3.5c.6 0 1 .4 1 1 0 1.3.2 2.5.6 3.6.1.3 0 .7-.2 1l-2.3 2.2z" fill="none" stroke="#4a5a3a" stroke-width="1.4"/>
          </svg>(770) 555-0148
        </p>
        <p class="contact__line">Fax (770) 555-0193</p>
        <p class="contact__line">www.DrColinHalvey.example</p>
      </div>
    </div>
  </div>
</body>
</html>
```